Lakeview Optiquip Partners Post Card

Lakeview Optiquip Partners. We buy, sell and service ophthalmic equipment for the eye care professional.
We sell New and Pre-Owned Chairs and Stands, Slit Lamps, Refractors, , Autolensometers, Perimeters, Autrefractor/Keratometer, Retinal Cameras and many more.
We also do a equipment repair, preventive maintenance, practice relocation and set-up and in-office service calls.

Target Market(s)

Opthalmologists, optometrist and all eye care professionals.

Industry/Entity Type

Medical Equipment

Font styles to use
Sans Serif

Colors
0355a3
33a6d7

Requirements
Must have
• My web site address: www.lakeviewoptiquip.example, tel. 555-718-4096, email: lakeviewlens@mailbox.example.
• I will mail the postcard, i need space for the postage and recipient address on the back.
Nice to have
• https://www.sketchhive.example/design/20472615
• https://www.sketchhive.example/design/20472608
• https://www.sketchhive.example/design/20439751

```html
<!DOCTYPE html>
<html lang="en">
<head>
<meta charset="utf-8">
<title>Lakeview Optiquip Partners Post Card</title>
<link rel="stylesheet" href="https://fonts.googleapis.com/css2?family=Open+Sans:wght@400;600;700;800&family=PT+Serif:wght@700&display=swap">
<style>
  :root {
    --brand-blue: #0355a3;
    --sky-blue: #33a6d7;
    --navy: #0b2f5c;
    --charcoal: #2a2c30;
    --pale-blue: #e4f1fa;
    --mist: #f3f8fc;
    --page: #e8ebee;
    --white: #ffffff;
    --ink: #2b3a4a;
    --rule: #b9c6d2;
  }
  * { box-sizing: border-box; margin: 0; padding: 0; }
  html, body { width: 880px; height: 1200px; overflow: hidden; }
  body {
    background: var(--page);
    font-family: "Open Sans", Arial, sans-serif;
    color: var(--ink);
    position: relative;
  }
  .postcard {
    position: absolute;
    left: 24px;
    width: 832px;
    height: 556px;
    background: var(--white);
    overflow: hidden;
    box-shadow: 0 4px 14px rgba(0,0,0,.22);
  }
  .postcard--front { top: 18px; }
  .postcard--back { top: 626px; }

  .backdrop { position: absolute; inset: 0; width: 100%; height: 100%; }

  .brand-name {
    position: absolute;
    font-family: "Open Sans", Arial, sans-serif;
    font-weight: 600;
    color: var(--brand-blue);
    text-transform: uppercase;
    letter-spacing: 1px;
    line-height: 1.25;
    display: flex;
    align-items: center;
    gap: 10px;
  }
  .brand-name .brand-dot {
    width: 14px; height: 14px; border-radius: 50%;
    background: var(--sky-blue); flex: none;
  }

  /* Front */
  .front-brand { left: 34px; top: 46px; width: 250px; font-size: 19px; }
  .service-panel {
    position: absolute; left: 0; top: 150px; width: 300px; height: 222px;
    background: var(--brand-blue);
    padding: 26px 20px 0 34px;
  }
  .service-list { list-style: none; }
  .service-list li {
    position: relative; color: var(--white); font-size: 15px;
    line-height: 1.28; padding-left: 22px; margin-bottom: 7px;
  }
  .service-list li svg { position: absolute; left: 0; top: 4px; }
  .contact-band {
    position: absolute; left: 0; bottom: 0; width: 300px; height: 184px;
    background: var(--charcoal); padding: 26px 0 0 34px; color: var(--white);
  }
  .contact-phone {
    display: flex; align-items: center; gap: 12px;
    font-size: 29px; font-weight: 700; margin-bottom: 14px;
  }
  .contact-line {
    display: flex; align-items: center; gap: 12px; font-size: 13px; margin-bottom: 10px;
  }
  .headline {
    position: absolute; left: 470px; top: 28px; width: 350px; text-align: center;
    font-family: "PT Serif", Georgia, serif; font-weight: 700;
  }
  .headline-main { color: var(--brand-blue); font-size: 35px; line-height: 1.08; text-transform: uppercase; }
  .headline-sub { color: var(--navy); font-size: 26px; line-height: 1.2; margin-top: 4px; }
  .equipment-photo {
    position: absolute; left: 318px; top: 184px; width: 500px; height: 360px;
    border-radius: 6px;
    background: linear-gradient(160deg, #f7f9fb 0%, #dfe6ec 55%, #c5d0da 100%);
  }

  /* Back */
  .buy-sell-band {
    position: absolute; left: 0; top: 0; width: 300px; height: 98px;
    background: var(--brand-blue); padding: 30px 0 0 34px;
    color: var(--white); font-size: 30px; font-weight: 800;
  }
  .intro {
    position: absolute; left: 34px; top: 110px; width: 250px;
    font-size: 13px; line-height: 1.3; text-transform: uppercase; color: var(--ink);
  }
  .body-copy {
    position: absolute; left: 34px; top: 176px; width: 240px;
    font-size: 12.5px; line-height: 1.4; color: var(--brand-blue);
  }
  .body-copy p { margin-bottom: 14px; }
  .body-copy strong { font-weight: 700; }
  .back-contact { height: 150px; padding-top: 22px; }
  .back-contact .contact-phone { font-size: 25px; margin-bottom: 10px; }
  .slit-lamp-photo {
    position: absolute; left: 300px; top: 96px; width: 200px; height: 440px;
    border-radius: 6px;
    background: linear-gradient(180deg, #f5f7f9 0%, #d8dee4 60%, #b9c3cc 100%);
  }
  .back-brand { left: 528px; top: 28px; width: 290px; font-size: 20px; justify-content: center; }
  .address-area {
    position: absolute; left: 540px; top: 238px; width: 270px;
  }
  .address-line { height: 1px; background: var(--rule); margin-bottom: 38px; }
  .stamp-box {
    position: absolute; right: 24px; top: 100px; width: 70px; height: 84px;
    border: 1px dashed var(--rule);
  }
  .divider {
    position: absolute; left: 515px; top: 110px; width: 1px; height: 380px; background: var(--rule);
  }
</style>
</head>
<body>

<section class="postcard postcard--front">
  <svg class="backdrop" viewBox="0 0 832 556" aria-hidden="true">
    <rect width="832" height="556" fill="var(--mist)"/>
    <polygon points="300,0 832,0 832,166 300,174" fill="var(--pale-blue)"/>
    <polygon points="300,160 420,0 470,0 330,168" fill="var(--sky-blue)" opacity=".85"/>
    <polygon points="300,162 832,154 832,168 300,176" fill="var(--brand-blue)"/>
    <polygon points="0,0 300,0 300,150 0,150" fill="var(--white)"/>
  </svg>

  <div class="brand-name front-brand"><span class="brand-dot"></span><span>Lakeview Optiquip Partners</span></div>

  <div class="service-panel">
    <ul class="service-list">
      <li><svg width="13" height="11" viewBox="0 0 13 11"><path d="M1 6l4 4 7-9" stroke="#fff" stroke-width="2" fill="none"/></svg>Full Service Department</li>
      <li><svg width="13" height="11" viewBox="0 0 13 11"><path d="M1 6l4 4 7-9" stroke="#fff" stroke-width="2" fill="none"/></svg>Repair and Maintenance</li>
      <li><svg width="13" height="11" viewBox="0 0 13 11"><path d="M1 6l4 4 7-9" stroke="#fff" stroke-width="2" fill="none"/></svg>In-Office Service Calls</li>
      <li><svg width="13" height="11" viewBox="0 0 13 11"><path d="M1 6l4 4 7-9" stroke="#fff" stroke-width="2" fill="none"/></svg>Chairs and Stands, Lane Maintenance and Urgent Repairs</li>
      <li><svg width="13" height="11" viewBox="0 0 13 11"><path d="M1 6l4 4 7-9" stroke="#fff" stroke-width="2" fill="none"/></svg>Practice Moves and Relocation's</li>
    </ul>
  </div>

  <div class="contact-band">
    <div class="contact-phone">
      <svg width="24" height="24" viewBox="0 0 24 24"><circle cx="12" cy="12" r="11" fill="none" stroke="#fff" stroke-width="2"/><path d="M8 6c1 0 2 2 2 3s-1 1-1 2 2 3 3 3 1-1 2-1 3 1 3 2-1 2-2 2c-3 0-9-6-9-9 0-1 1-2 2-2z" fill="#fff"/></svg>
      <span>555-718-4096</span>
    </div>
    <div class="contact-line">
      <svg width="16" height="12" viewBox="0 0 16 12"><rect x="1" y="1" width="14" height="10" fill="none" stroke="#fff" stroke-width="1.5"/><path d="M1 1l7 6 7-6" fill="none" stroke="#fff" stroke-width="1.5"/></svg>
      <span>lakeviewlens@mailbox.example</span>
    </div>
    <div class="contact-line">
      <svg width="16" height="16" viewBox="0 0 16 16"><circle cx="8" cy="8" r="7" fill="none" stroke="#fff" stroke-width="1.5"/><path d="M1 8h14M8 1c3 3 3 11 0 14M8 1c-3 3-3 11 0 14" fill="none" stroke="#fff" stroke-width="1.2"/></svg>
      <span>www.lakeviewoptiquip.example</span>
    </div>
  </div>

  <div class="headline">
    <div class="headline-main">Top Quality<br>Eye Exam</div>
    <div class="headline-sub">Equipment For Less!</div>
  </div>

  <div class="equipment-photo" role="img" aria-label="Photograph of an automatic lensmeter and an autorefractor side by side"></div>
</section>

<section class="postcard postcard--back">
  <svg class="backdrop" viewBox="0 0 832 556" aria-hidden="true">
    <rect width="832" height="556" fill="var(--white)"/>
    <polygon points="500,0 832,0 832,90 560,90" fill="var(--pale-blue)"/>
    <polygon points="300,0 380,0 330,98 300,98" fill="var(--sky-blue)" opacity=".8"/>
  </svg>

  <div class="buy-sell-band">WE BUY / SELL</div>
  <p class="intro">And service ophthalmic equipment for the eye care professional.</p>
  <div class="body-copy">
    <p>We sell <strong>New and Pre-Owned Chairs and Stands, Slit Lamps, Refractors, Autolensometers, Perimeters, Autorefractor/Keratometer, Retinal Cameras</strong> and many more.</p>
    <p>We also do a equipment repair, preventive maintenance, practice relocation and set up and in-office service calls.</p>
  </div>

  <div class="contact-band back-contact">
    <div class="contact-phone">
      <svg width="22" height="22" viewBox="0 0 24 24"><circle cx="12" cy="12" r="11" fill="none" stroke="#fff" stroke-width="2"/><path d="M8 6c1 0 2 2 2 3s-1 1-1 2 2 3 3 3 1-1 2-1 3 1 3 2-1 2-2 2c-3 0-9-6-9-9 0-1 1-2 2-2z" fill="#fff"/></svg>
      <span>555-718-4096</span>
    </div>
    <div class="contact-line">
      <svg width="16" height="12" viewBox="0 0 16 12"><rect x="1" y="1" width="14" height="10" fill="none" stroke="#fff" stroke-width="1.5"/><path d="M1 1l7 6 7-6" fill="none" stroke="#fff" stroke-width="1.5"/></svg>
      <span>lakeviewlens@mailbox.example</span>
    </div>
    <div class="contact-line">
      <svg width="16" height="16" viewBox="0 0 16 16"><circle cx="8" cy="8" r="7" fill="none" stroke="#fff" stroke-width="1.5"/><path d="M1 8h14M8 1c3 3 3 11 0 14M8 1c-3 3-3 11 0 14" fill="none" stroke="#fff" stroke-width="1.2"/></svg>
      <span>www.lakeviewoptiquip.example</span>
    </div>
  </div>

  <div class="slit-lamp-photo" role="img" aria-label="Photograph of a slit lamp microscope on a table"></div>

  <div class="brand-name back-brand"><span class="brand-dot"></span><span>Lakeview Optiquip Partners</span></div>

  <div class="divider"></div>
  <div class="stamp-box" aria-label="Postage area"></div>
  <div class="address-area" aria-label="Recipient address">
    <div class="address-line"></div>
    <div class="address-line"></div>
    <div class="address-line"></div>
    <div class="address-line"></div>
  </div>
</section>

</body>
</html>
```